Commercial Cleaning Company Needs A Flyer

We are a commercial cleaning company based in London.
We are currently trying to grow our client base and would like a fresh, professional flyer that differentiates us from the competition. We mainly specialises in commercial cleaning such as offices, educational facilities etc. I would like to see a flyer design that look professional, unique not cheap. I have attached a file that contains some company details but Im happy to explore other options if thay are relevant. Please also find company logo and colour chart, this should remain as is.

I have attached some pictures that contain diamond shaped windows. I feel that this can be used to represent and incorporate the logo. Please add to flyer where possible.

Please feel free to contact me for any further advice.
Thanks and good luck

Target Market(s)

commercial buildings and residential property owners

Industry/Entity Type

Cleaning Service

Contact Information for Business Card

Please refer to up loaded document for company details and logo colours.

Font styles to use
Sans Serif

Colors
33a6d7
33b8a4

Requirements
Must have
• Look Professional, not cheap, unique, stand out from others.

```html
<!DOCTYPE html>
<html lang="en">
<head>
<meta charset="utf-8">
<title>Clearwell Services Flyer</title>
<link href="https://fonts.googleapis.com/css2?family=Arimo:wght@400;700&display=swap" rel="stylesheet">
<style>
  :root {
    --mint: #52dcc6;
    --sky: #5bbcef;
    --brand: #33a6d7;
    --ink: #1b1b1b;
    --grey-ink: #3a3a3a;
    --paper: #ffffff;
    --tint: #f2fafa;
    --pattern: #dcf3f4;
    --backdrop: #e8e8e8;
  }
  * { margin: 0; padding: 0; box-sizing: border-box; }
  html, body { width: 1200px; height: 800px; overflow: hidden; }
  body {
    background: var(--backdrop);
    font-family: "Arimo", Arial, sans-serif;
    color: var(--ink);
    position: relative;
  }
  .page {
    position: absolute;
    top: 42px;
    width: 492px;
    height: 702px;
    background: var(--paper);
    overflow: hidden;
  }
  .page--front { left: 72px; background: linear-gradient(180deg, var(--tint), var(--paper) 60%); }
  .page--back { left: 628px; }
  .page svg.art { position: absolute; inset: 0; width: 492px; height: 702px; }

  .brand { position: absolute; display: flex; align-items: center; }
  .brand__dot { border-radius: 50%; background: var(--brand); flex: none; }
  .brand__name { color: var(--brand); font-weight: 700; white-space: nowrap; }
  .brand__tag { color: var(--grey-ink); font-weight: 400; white-space: nowrap; }

  .brand--front { left: 16px; top: 14px; }
  .brand--front .brand__dot { width: 30px; height: 30px; margin-right: 12px; }
  .brand--front .brand__name { font-size: 17px; line-height: 19px; }
  .brand--front .brand__tag { font-size: 10px; line-height: 13px; }

  .brand--back { left: 326px; top: 660px; }
  .brand--back .brand__dot { width: 20px; height: 20px; margin-right: 8px; }
  .brand--back .brand__name { font-size: 11px; line-height: 12px; }
  .brand--back .brand__tag { font-size: 7.4px; line-height: 9px; }

  .about {
    position: absolute; left: 226px; top: 342px; width: 246px;
    font-size: 10.3px; line-height: 12.2px; font-weight: 700;
  }
  .about p + p { margin-top: 12.2px; }

  .contact { position: absolute; font-weight: 700; }
  .contact--front { left: 33px; top: 598px; font-size: 10.6px; line-height: 12.9px; }
  .contact--front h3 { font-size: 10.8px; margin-bottom: 13px; }
  .contact--back { left: 10px; top: 596px; font-size: 13.6px; line-height: 17px; }
  .contact--back h3 { font-size: 13.6px; margin-bottom: 17px; }

  .footer-band { position: absolute; left: 0; bottom: 0; width: 100%; height: 16px; display: flex; }
  .footer-band span:first-child { width: 50%; background: var(--mint); }
  .footer-band span:last-child { width: 50%; background: var(--sky); }

  .promise { position: absolute; left: 18px; top: 24px; font-weight: 700; }
  .promise__lead { font-size: 9.6px; line-height: 12.4px; }
  .promise__list { list-style: none; margin-top: 13px; font-size: 9.6px; line-height: 16.2px; }
  .promise__list b { font-size: 12px; }

  .divider { position: absolute; left: 18px; top: 213px; width: 301px; height: 2px; background: var(--mint); }

  .aim { position: absolute; left: 18px; top: 239px; font-size: 13.6px; line-height: 17.6px; font-weight: 700; }

  .services { position: absolute; }
  .services h4 { font-size: 10px; line-height: 12.2px; font-weight: 700; text-decoration: underline; }
  .services ul { list-style: none; }
  .services li { position: relative; padding-left: 30px; font-size: 9.8px; line-height: 12.2px; }
  .services li::before { content: "▪"; position: absolute; left: 0; font-size: 4px; color: #bbbbbb; }
  .services--strong li { font-weight: 700; }
  .services--light li { font-weight: 400; color: var(--grey-ink); font-size: 9px; }
  .services li.wrap span { display: block; margin-left: -20px; }
  .col-commercial { left: 19px; top: 290px; }
  .col-services { left: 19px; top: 375px; }
  .col-residential { left: 242px; top: 290px; }
  .col-green { left: 242px; top: 387px; }
</style>
</head>
<body>

<section class="page page--front">
  <svg class="art" viewBox="0 0 615 878">
    <defs>
      <linearGradient id="roofTone" x1="0" y1="0" x2="1" y2="1">
        <stop offset="0" stop-color="#6c6c6c"/>
        <stop offset="0.5" stop-color="#3d3d3d"/>
        <stop offset="1" stop-color="#1e1e1e"/>
      </linearGradient>
      <linearGradient id="windowTone" x1="0" y1="0" x2="1" y2="1">
        <stop offset="0" stop-color="#d9dde0"/>
        <stop offset="0.6" stop-color="#9aa4ac"/>
        <stop offset="1" stop-color="#5f6a72"/>
      </linearGradient>
    </defs>
    <path d="M378 0 L402 0 L262 200 L238 208 Z" fill="#52dcc6"/>
    <path d="M395 0 L615 0 L615 376 Q450 352 300 335 Q258 290 252 204 Z" fill="url(#roofTone)" role="img" aria-label="Glass roof with triangular lattice seen from below"/>
    <path d="M540 370 L615 374 L606 396 Z" fill="#52dcc6"/>
    <circle cx="203" cy="306" r="105" fill="url(#windowTone)" role="img" aria-label="City skyline seen through diamond-shaped windows"/>
    <circle cx="90" cy="488" r="63" fill="url(#windowTone)" role="img" aria-label="Office towers seen through diamond window frames"/>
  </svg>

  <div class="brand brand--front">
    <span class="brand__dot"></span>
    <div>
      <div class="brand__name">Clearwell Services</div>
      <div class="brand__tag">Commercial cleaning across London</div>
    </div>
  </div>

  <div class="about">
    <p>Clearwell Services continual commitment and dedication to delivering a quality service has enabled us to build a solid foundation within the cleaning industry.</p>
    <p>Our principle and objectives are simple, provide our customers with an affordable quality service to suit their needs and always put our clients first.</p>
    <p>CWS rewards dependability, integrality and provide the training and development for all employees to achieve the best possible results. We believe that building relationships based on ethical conduct towards employees and clientele defines our unique working environments and is a vital key to our success.</p>
  </div>

  <div class="contact contact--front">
    <h3>Company Contact Details</h3>
    <div>Email: enquiries@clearwellservices.com</div>
    <div>Web:clearwellservices.com</div>
    <div>Mobile: 07900123456</div>
    <div>Office:02081234567</div>
  </div>

  <div class="footer-band"><span></span><span></span></div>
</section>

<section class="page page--back">
  <svg class="art" viewBox="0 0 615 878">
    <path d="M355 0 L615 0 L615 878 L260 878 L555 410 Z" fill="#dcf3f4" role="img" aria-label="Faint geometric diamond window pattern"/>
  </svg>

  <div class="promise">
    <p class="promise__lead">This is why at Clearwell Services stand<br>behind our performance and guarantee your satisfaction.</p>
    <ul class="promise__list">
      <li><b>Q</b>uick response to costumers needs guaranteed</li>
      <li><b>U</b>nequal attention to detail</li>
      <li><b>A</b>ffordable cleaning tailored to your needs</li>
      <li><b>L</b>engthy industry experience</li>
      <li><b>I</b>nsurance inclusive of Workers Compensation and Liability</li>
      <li><b>T</b>raining provided to all staff and supervisors</li>
      <li><b>Y</b>our satisfaction is our priority</li>
    </ul>
  </div>

  <div class="divider"></div>

  <h2 class="aim">We aim to offer the highest<br>Commercial and Residential cleaning standards.</h2>

  <div class="services services--strong col-commercial">
    <h4>Commercial Cleaning</h4>
    <ul>
      <li>Offices</li>
      <li>Education Facilities</li>
      <li>Medical Facilities</li>
      <li>Restaurants</li>
      <li>Showroom</li>
    </ul>
  </div>

  <div class="services services--strong col-services">
    <h4>Services</h4>
    <ul>
      <li>General Cleaning Requirements</li>
      <li class="wrap">Consumables supply and<span>replacement</span></li>
      <li>Washroom services</li>
      <li>Building maintenance</li>
      <li>Window cleaning</li>
      <li>Carpet care</li>
      <li>Floor maintenance</li>
      <li>Scrubbing machinery</li>
      <li>PAT Testing</li>
      <li>Waste removal</li>
      <li>Recycling Programs</li>
    </ul>
  </div>

  <div class="services services--light col-residential">
    <h4>Residential Cleaning</h4>
    <ul>
      <li>House Cleaning</li>
      <li>Apartment Cleaning</li>
      <li>Move In/Out Cleaning</li>
      <li>After Event Cleaning</li>
      <li>Spring Cleaning</li>
      <li>Post Building Works Deep Clean</li>
    </ul>
  </div>

  <div class="services services--light col-green">
    <h4>Green Cleaning Available</h4>
    <ul>
      <li>No harmful chemicals</li>
      <li>safe for children and pets</li>
      <li>eco-friendly</li>
      <li>no artificial fragrances</li>
    </ul>
  </div>

  <div class="contact contact--back">
    <h3>Company Contact Details</h3>
    <div>enquiries@clearwellservices.com</div>
    <div>Wclearwellservices.com</div>
    <div>Mobile: 07900123456</div>
    <div>Office:02081234567</div>
  </div>

  <div class="brand brand--back">
    <span class="brand__dot"></span>
    <div>
      <div class="brand__name">Clearwell Services</div>
      <div class="brand__tag">Commercial cleaning across London</div>
    </div>
  </div>
</section>

</body>
</html>
```